Service Menu refresh 2018 Update of menu pricing

We currently have service menus as attached. We will be updating our look via our homepage image, our service menu and our in-house beverage and treatment menu.
We are a natural and sustainable hair salon group and moving more towards head spa which consists of treatments, beauty, tanning as well as your traditional hair services. Our imagery needs to reflect our efforts in spa treatments in the hair and scalp area and use natural materials and colours reflecting sustainability.
Velin is the brand we stock and promote.

Target Market(s)

Men or women interesting in personal maintenance with natural and organic products and using sustainable practises

Industry/Entity Type

Hair And Beauty

Font styles to use
Sans Serif
Other font styles liked:
• Arial or Helvetica

Colors
9acb3c
abd037
cadf82
ffffff

Requirements
Must have
• Name on the front cover, locations on back cover
Nice to have
• Prestige feel, reflect male and female clients
Should not have
• Bold artificial writing or any type of cartoon images.
• Same images as existing menu.

```html
<!DOCTYPE html>
<html lang="en">
<head>
<meta charset="utf-8">
<title>Verdant Roots – Salon Card</title>
<link href="https://fonts.googleapis.com/css2?family=Arimo:wght@400;700&display=swap" rel="stylesheet">
<style>
  :root {
    --backdrop: #5b5b5b;
    --card: #f7fbe0;
    --card-soft: #eef6cf;
    --frame: #abd037;
    --band: #9acb3c;
    --leaf-dark: #3f7f2a;
    --leaf-pale: #cfe3a6;
    --blossom: #f4898b;
    --blossom-soft: #f9c3c1;
    --fern: #6fb3b8;
    --ink: #1e1e1e;
    --white: #ffffff;
  }
  * { box-sizing: border-box; margin: 0; padding: 0; }
  html, body { width: 1200px; height: 1200px; overflow: hidden; }
  body {
    background: var(--backdrop);
    font-family: "Arimo", Arial, Helvetica, sans-serif;
    color: var(--ink);
    position: relative;
  }
  .card {
    position: absolute;
    left: 170px;
    width: 862px;
    height: 470px;
    background: radial-gradient(ellipse at 55% 50%, var(--card) 40%, var(--card-soft) 100%);
    overflow: hidden;
    box-shadow: 0 6px 18px rgba(0,0,0,0.35);
  }
  .card--front { top: 106px; }
  .card--back { top: 625px; }
  .card__frame {
    position: absolute;
    left: 30px; top: 30px;
    width: 800px; height: 410px;
    border: 2px solid var(--frame);
  }
  .foliage {
    position: absolute;
    background: linear-gradient(135deg, var(--leaf-dark), var(--leaf-pale));
    opacity: 0.55;
  }
  .foliage--front-left {
    left: -60px; top: -40px; width: 260px; height: 560px;
    border-radius: 0 60% 60% 0;
  }
  .floral-wreath {
    position: absolute;
    left: 410px; top: 98px; width: 424px; height: 356px;
    border-radius: 46%;
    background: radial-gradient(ellipse at 50% 50%, var(--fern) 0%, var(--fern) 45%, var(--blossom-soft) 80%, var(--blossom) 100%);
  }
  .brand-panel {
    position: absolute;
    left: 501px; top: 194px; width: 256px; height: 152px;
    background: var(--white);
    border: 2px solid var(--frame);
    outline: 4px solid var(--white);
    display: flex; align-items: center; justify-content: center;
  }
  .brand {
    display: flex; align-items: center; gap: 9px;
    font-weight: 400; color: var(--ink);
  }
  .brand__dot {
    width: 30px; height: 30px; border-radius: 50%;
    background: var(--band);
    flex: none;
  }
  .brand__name { font-size: 24px; letter-spacing: 0.2px; }
  .quote { position: absolute; left: 155px; top: 48px; }
  .quote__mark {
    display: block; color: var(--band);
    font-size: 48px; font-weight: 700; line-height: 40px; height: 24px;
    overflow: hidden;
  }
  .quote__text { font-size: 16px; line-height: 21px; margin-top: 4px; }
  .quote__close { color: var(--band); font-weight: 700; }
  .web-band {
    position: absolute;
    width: 237px; height: 21px;
    background: var(--band);
    color: var(--ink);
    font-size: 11px; font-style: italic; letter-spacing: 2.2px;
    display: flex; align-items: center; justify-content: center;
  }
  .web-band--front { left: 156px; top: 146px; }
  .web-band--back { left: 413px; top: 430px; }

  .foliage--back-top {
    left: 600px; top: -60px; width: 320px; height: 300px;
    border-radius: 0 0 0 70%;
  }
  .foliage--back-bottom {
    left: 760px; top: 300px; width: 140px; height: 200px;
    border-radius: 70% 0 0 0;
  }
  .addresses__title {
    position: absolute; left: 61px; top: 144px;
    font-size: 20px; font-weight: 700; letter-spacing: 0.3px;
  }
  .location { position: absolute; font-size: 10.5px; line-height: 13px; }
  .location__name { font-weight: 700; }
  .location--a { left: 61px; top: 182px; }
  .location--b { left: 412px; top: 182px; }
  .location--c { left: 61px; top: 262px; }
  .location--d { left: 412px; top: 262px; }
  .location--e { left: 412px; top: 338px; }
  .brand--back { position: absolute; left: 59px; top: 361px; }
</style>
</head>
<body>

<section class="card card--front">
  <div class="foliage foliage--front-left" role="img" aria-label="Green leafy branches, some softly blurred"></div>
  <div class="card__frame"></div>
  <div class="quote">
    <span class="quote__mark">&ldquo;</span>
    <p class="quote__text">Living a more natural and<br>organic life is a philosophy<br>not just a product certification..<span class="quote__close">&rdquo;</span></p>
  </div>
  <div class="web-band web-band--front">www.verdantroots.com.au</div>
  <div class="floral-wreath" role="img" aria-label="Wreath of coral tropical flowers, teal fern fronds and small berries"></div>
  <div class="brand-panel">
    <div class="brand">
      <span class="brand__dot"></span>
      <span class="brand__name">Verdant Roots</span>
    </div>
  </div>
</section>

<section class="card card--back">
  <div class="foliage foliage--back-top" role="img" aria-label="Green leafy branch"></div>
  <div class="foliage foliage--back-bottom" role="img" aria-label="Green leaves"></div>
  <div class="card__frame"></div>

  <h2 class="addresses__title">OUR ADDRESS</h2>

  <div class="location location--a">
    <p class="location__name">Larkwood</p>
    <p>Shop 104 Larkwood Plaza, Fennel Rd, Larkwood</p>
    <p>+61 (07) 3100 4821</p>
    <p>larkwood@verdantroots.com.au</p>
  </div>
  <div class="location location--b">
    <p class="location__name">Millbrook</p>
    <p>Shop 27 Millbrook Central, Tansy Road, Millbrook</p>
    <p>+61 (07) 3100 4821</p>
    <p>millbrook@verdantroots.com.au</p>
  </div>
  <div class="location location--c">
    <p class="location__name">Eastmere</p>
    <p>Shop 3310 Eastmere Shopping Centre, Sorrel Rd Eastmere.</p>
    <p>+61 (07) 3100 5932</p>
    <p>eastmere@verdantroots.com.au</p>
  </div>
  <div class="location location--d">
    <p class="location__name">Oakhaven</p>
    <p>Shop 1182 Oakhaven Square, Juniper St, Oakhaven</p>
    <p>+61 (07) 31006147</p>
    <p>oakhaven@verdantroots.com.au</p>
  </div>
  <div class="location location--e">
    <p class="location__name">Riverbend Medical Centre</p>
    <p>Willow St. Riverbend Qld 4999</p>
    <p>+61 (07) 3100 7260</p>
    <p>riverbend@verdantroots.com.au</p>
  </div>

  <div class="brand brand--back">
    <span class="brand__dot"></span>
    <span class="brand__name">Verdant Roots</span>
  </div>

  <div class="web-band web-band--back">www.verdantroots.com.au</div>
</section>

</body>
</html>
```